Webdesign plus CSS for a German company data register

We need a unique and attractive webdesign including CSS development for a website (https://kontorblick.de/) of our newly founded company. We collect company data from several public registers to display them aggregated.

Your design should communicate science, data security, a business note and perhaps a slice of nerdness. Elements - like color and layout - of our logo should also be found in your design.

Target Market(s)

banks, insurance companies, authorities etc.

Industry/Entity Type

Internet

Coding

Coded - Design and coding required

Number of Pages Required

3 page

Font styles to use
Sans Serif

Requirements
Must have
• mockups, CSS

eye catching, easy to read / navigate
Nice to have
• pictogramms / logos for essential content

```html
<!DOCTYPE html>
<html lang="de">
<head>
<meta charset="utf-8">
<title>Kontorblick – Firmen suche</title>
<link href="https://fonts.googleapis.com/css2?family=Open+Sans:wght@400;600;700&display=swap" rel="stylesheet">
<style>
:root{
  --orange:#ff5312;
  --dark:#505050;
  --text:#444;
  --muted:#9a9a9a;
  --field:#d9d9d9;
  --line:#e2e2e2;
  --white:#fff;
}
*{box-sizing:border-box;margin:0;padding:0}
html,body{width:1200px;height:889px;overflow:hidden;background:var(--white);font-family:"Open Sans",sans-serif;color:var(--text)}
.page{position:relative;width:1200px;height:889px}
.abs{position:absolute}
.header{position:absolute;left:0;top:0;width:1200px;height:45px;background:var(--white);box-shadow:0 2px 4px rgba(0,0,0,.12)}
.corner{position:absolute;left:0;top:0}
.brand{position:absolute;left:158px;top:14px;font-size:14px;font-weight:700;color:var(--orange);letter-spacing:.5px}
.nav a{position:absolute;top:13px;font-size:11.5px;font-weight:600;letter-spacing:1.3px;color:var(--dark);text-decoration:none}
.nav .active::after{content:"";position:absolute;left:-9px;right:-7px;top:19px;height:2px;background:var(--orange)}
.btn{position:absolute;background:var(--orange);color:var(--white);font-size:12px;display:flex;align-items:center;justify-content:center;box-shadow:0 2px 3px rgba(0,0,0,.15)}
.lang{position:absolute;left:1090px;top:13px;font-size:11.5px;font-weight:600;color:var(--dark)}
.lang::after{content:"";display:inline-block;margin-left:5px;border:4px solid transparent;border-top:5px solid var(--dark);border-bottom:0;vertical-align:2px}
.title{position:absolute;left:0;width:1200px;top:126px;text-align:center;font-size:24px;font-weight:600;letter-spacing:1px;color:var(--dark)}
.title span{color:var(--orange)}
.search-field{left:444px;top:198px;width:220px;height:28px;background:var(--field)}
.count{left:256px;top:244px;font-size:11px}
.results{left:240px;top:272px;width:720px;height:94px;background:var(--white);box-shadow:0 1px 4px rgba(0,0,0,.12)}
.results .head{position:absolute;left:0;top:0;width:580px;height:30px;border-bottom:1px solid var(--line);font-size:11px;padding:8px 0 0 22px}
.results .dob{position:absolute;left:580px;top:0;width:140px;height:94px;background:var(--dark);color:var(--white);font-size:11px;text-align:center;padding-top:8px}
.results .dob::after{content:"";position:absolute;left:0;right:0;top:30px;height:1px;background:#6a6a6a}
.notes{left:382px;top:490px;width:440px;font-size:10.5px;line-height:12.5px}
.notes li{list-style:none;position:relative;padding-left:15px;margin-bottom:15px}
.notes li::before{content:"";position:absolute;left:0;top:4px;width:5px;height:5px;border-radius:50%;background:var(--dark)}
.hint{left:399px;top:569px;font-size:10.5px}
.band{left:0;top:676px;width:1200px;height:47px;background:var(--dark);color:var(--white);text-align:center;font-size:10.5px;font-weight:700;letter-spacing:1px;padding-top:16px}
.band a{color:var(--orange);margin-left:8px;text-decoration:none}
.footer{top:857px;font-size:10.5px}
.footer.link{color:var(--orange)}
</style>
</head>
<body>
<div class="page">
  <header class="header">
    <svg class="corner" width="120" height="45" viewBox="0 0 120 45" aria-hidden="true">
      <polygon points="0,0 44,0 83,45 0,45" fill="#ff5312"/>
      <polygon points="44,0 78,0 117,45 83,45" fill="#505050"/>
    </svg>
    <div class="brand">KONTORBLICK</div>
    <nav class="nav">
      <a style="left:669px">Start</a>
      <a class="active" style="left:719px">Firmen</a>
      <a style="left:783px">Personen</a>
      <a style="left:863px">Statistiken</a>
    </nav>
    <div class="btn" style="left:956px;top:9px;width:87px;height:27px">Kontakt</div>
    <div class="lang">DE</div>
  </header>

  <h1 class="title">Firmen suche in <span>Kontorblick</span></h1>

  <div class="abs search-field"></div>
  <div class="btn" style="left:664px;top:197px;width:87px;height:30px">Suche</div>

  <div class="abs count">0 Ergebnisse gefunden</div>

  <div class="abs results">
    <div class="head">Nachname, Vorname</div>
    <div class="dob">Geburtsdatum</div>
  </div>

  <ul class="abs notes">
    <li>Sofern Sie einen fehlerhaften Eintrag finden würden wir uns über Ihr Feedback freuen</li>
    <li>Sofern Sie Ihren eigenen Eintrag verbessern oder ergänzen wollen, sind Sie herzlich<br>&nbsp;eingeladen dies zu tun</li>
  </ul>
  <div class="abs hint">Nutzen Sie in beiden Fällen bitte unser Kontaktformular</div>
  <div class="btn" style="left:536px;top:602px;width:87px;height:28px">Kontakt</div>

  <div class="abs band">Datenschutz steht bei uns an erster Stelle. sehen <a>Datenschutz</a></div>

  <div class="abs footer" style="left:414px">© 2020 - Kontorblick</div>
  <div class="abs footer link" style="left:646px">Impressum</div>
  <div class="abs footer link" style="left:733px">Datenschutz</div>
</div>
</body>
</html>
```